Hound Ridge Detection Services

We seek a website that will attract our customer base ( School Districts, Private, Charter Schools, Rehabilitation Centers, and Presidential Customers ( parents). The website should describe it's viewers with written and visual examples and examples of the K9 Detection Services we provide. In addition, we would like to have an educational section on the website to post ant-drug and vape materials for our client schools and parents. Lastly, a "how to contact us" with social media links, email, and phone number.
Updates

In addition to the development of a website, I will need to incorporate a business email to the domain name.

Target Market(s)

Public School Districts, Private Schools, Charter Schools, Residential ( Parents), and Rehabilitation Centers

Industry/Entity Type

K9 Detection

Coding

Coded - Design and coding required

Number of Pages Required

2 page

Font styles to use
Sans Serif

Colors
0054AA
0677BA
7BADD7
CADEEF
E8F1F8

Requirements
Must have
• Explanation/Examples of Services( Written, Pictures,Videos), Levels of Service Plans, Testimonials, Contact Information
Nice to have
• Educational Section, FAQs,
Should not have
• I can't think of anything.

```html
<!DOCTYPE html>
<html lang="en">
<head>
<meta charset="UTF-8">
<title>Hound Ridge Detection Services</title>
<link href="https://fonts.googleapis.com/css2?family=Roboto:wght@400;500;700&display=swap" rel="stylesheet">
<style>
:root{
  --blue-dark:#0054AA;
  --blue:#0677BA;
  --blue-mid:#7BADD7;
  --blue-light:#CADEEF;
  --blue-pale:#E8F1F8;
  --text:#333;
  --muted:#6b6b6b;
  --grey-bg:#f3f4f6;
}
*{box-sizing:border-box;margin:0;padding:0}
html,body{width:1200px;height:3955px;overflow:hidden}
body{font-family:'Roboto',sans-serif;color:var(--text);position:relative;background:#fff}
.abs{position:absolute}
a{color:inherit;text-decoration:none}

.topbar{left:0;top:0;width:1200px;height:48px;background:var(--blue-dark);color:#fff;font-size:15px}
.topbar span{position:absolute;top:14px;display:flex;align-items:center;gap:6px}
.navbar{left:0;top:48px;width:1200px;height:72px;background:#fff}
.nav-item{position:absolute;top:26px;font-size:15px;color:#555}
.nav-item.active{color:var(--blue-dark);font-weight:700}
.brand{left:120px;top:12px;width:126px;height:142px;z-index:5;display:flex;align-items:center;justify-content:center}
.brand-circle{width:126px;height:126px;border-radius:50%;background:#fff;box-shadow:0 2px 8px rgba(0,0,0,.25);display:flex;align-items:center;justify-content:center;text-align:center;font-size:14px;font-weight:700;color:var(--blue-dark);line-height:1.25;padding:12px}

.hero{left:0;top:120px;width:1200px;height:494px;background:linear-gradient(90deg,#3c2a22 0%,#5a4033 30%,#6d5545 47%,#8aa6c4 48%,#a9bfd6 70%,#6f6458 100%)}
.hero-title{left:112px;top:243px;font-size:45px;font-weight:700;color:#fff;line-height:1.22}
.hero-text{left:112px;top:384px;width:440px;font-size:17px;color:#fff;line-height:1.5}
.btn{display:flex;align-items:center;justify-content:center;font-size:15px}
.hero-btn{left:112px;top:447px;width:118px;height:38px;background:var(--blue);color:#fff}

.section-title{left:0;width:1200px;text-align:center;font-size:36px;font-weight:500;color:var(--blue-dark)}
.service-card{width:232px;height:290px;background:#fff;box-shadow:0 2px 12px rgba(0,0,0,.15);border-radius:6px;text-align:center;padding-top:25px}
.icon-circle{width:97px;height:97px;border-radius:50%;background:var(--blue);margin:0 auto;display:flex;align-items:center;justify-content:center}
.service-card h3{margin-top:22px;font-size:19px;font-weight:500;color:var(--blue-dark)}
.service-card p{margin:10px auto 0;width:190px;font-size:13px;color:var(--muted);line-height:1.6}
.service-card .more{display:inline-block;margin-top:10px;font-size:13px;color:var(--blue);text-decoration:underline}

.edu{left:0;top:1211px;width:1200px;height:589px;background:linear-gradient(90deg,#0a5cad,#0d66b7 60%,#1a6db6)}
.edu-ring{left:108px;top:1300px;width:430px;height:420px}
.edu-photo{left:112px;top:1314px;width:390px;height:390px;border-radius:50%;background:linear-gradient(160deg,#dfe6ee,#b8c6d6 50%,#8a7a66)}
.edu h2{}
.edu-title{left:600px;top:1322px;font-size:38px;font-weight:500;color:#fff}
.edu-text{left:600px;top:1399px;width:490px;font-size:15px;line-height:1.73;color:#fff}
.edu-btn{left:600px;top:1645px;width:118px;height:38px;background:var(--blue);color:#fff}

.plans{left:0;top:1800px;width:1200px;height:679px;background:var(--grey-bg)}
.plan{top:1968px;width:300px;height:425px;background:#fff;border-radius:10px;box-shadow:0 2px 10px rgba(0,0,0,.08);text-align:center}
.plan h3{margin-top:20px;font-size:24px;font-weight:500;color:var(--blue-dark)}
.plan .sub{margin-top:10px;font-size:14px;color:var(--muted)}
.plan hr{border:0;border-top:1px solid #ddd;margin:18px 10px 0}
.plan ul{list-style:none;text-align:left;padding:10px 0 0 34px}
.plan li{height:28.3px;font-size:14px;display:flex;align-items:center;gap:12px;color:#444}
.plan .btn{position:absolute;left:55px;top:374px;width:190px;height:37px;background:var(--blue-dark);color:#fff}
.plan.featured{background:var(--blue);color:#fff}
.plan.featured h3,.plan.featured .sub,.plan.featured li{color:#fff}
.plan.featured hr{border-color:rgba(255,255,255,.35)}
.plan.featured .btn{background:#fff;color:var(--blue)}
.plan .line-bottom{position:absolute;left:10px;right:10px;top:356px;border-top:1px solid #ddd}
.plan.featured .line-bottom{border-color:rgba(255,255,255,.35)}

.review{top:2648px;width:450px;height:200px;background:#fff;border-radius:6px;box-shadow:0 2px 12px rgba(0,0,0,.13)}
.review .q{position:absolute;left:24px;top:378px}
.review p{position:absolute;left:26px;top:57px;width:400px;font-size:15px;line-height:1.7;color:#555}
.review .stars{position:absolute;left:26px;top:168px;font-size:16px;color:#333;display:flex;align-items:center;gap:8px}
.review .tail{position:absolute;left:60px;bottom:-12px;width:24px;height:24px;background:#fff;transform:rotate(45deg);box-shadow:3px 3px 6px rgba(0,0,0,.06)}
.reviewer{display:flex;align-items:center;gap:20px}
.avatar{width:74px;height:74px;border-radius:50%;background:linear-gradient(160deg,#d4d7db,#7b8794)}
.reviewer h4{font-size:20px;font-weight:500;color:var(--blue-dark)}
.reviewer span{font-size:14px;color:#444}

.divider{left:112px;top:3047px;width:976px;border-top:1px solid #999}
.faq-title{left:112px;top:3124px;font-size:36px;font-weight:500;color:var(--blue-dark)}
.faq{left:112px;width:479px;height:64px;border-bottom:1px solid #999;font-size:16px;color:#333;display:flex;align-items:center;justify-content:space-between;padding-top:6px}
.faq-dog{left:652px;top:3124px;width:476px;height:391px;background:radial-gradient(ellipse at 50% 55%,#8a5a2e 0%,#5b3a20 40%,rgba(255,255,255,0) 70%)}

.footer{left:0;top:3596px;width:1200px;height:359px;background:var(--blue-dark);color:#fff}
.footer h4{font-size:20px;font-weight:500}
.footer h4::after{content:"";display:block;width:56px;height:2px;background:#fff;margin-top:6px}
.footer ul{list-style:none;margin-top:18px}
.footer li{font-size:14px;height:26px}
.foot-brand{left:107px;top:3653px;width:170px;height:137px;display:flex;align-items:center;gap:10px;font-size:17px;font-weight:700;line-height:1.3}
.foot-brand .dot{width:40px;height:40px;border-radius:50%;background:#fff;flex:none}
.socials{left:110px;top:3821px;display:flex;gap:7px}
.socials span{width:31px;height:31px;border-radius:50%;border:2px solid #fff}
.contact-row{display:flex;gap:20px;font-size:14px;line-height:1.5;margin-bottom:12px}
.copy{left:0;top:3890px;width:1200px;border-top:1px solid rgba(255,255,255,.35);text-align:center;padding-top:20px;font-size:14px}
</style>
</head>
<body>

<div class="abs topbar">
  <span style="left:640px">
    <svg width="14" height="14" viewBox="0 0 24 24" fill="#fff"><path d="M6.6 10.8a15.1 15.1 0 006.6 6.6l2.2-2.2c.3-.3.7-.4 1-.2 1.1.4 2.3.6 3.6.6.6 0 1 .4 1 1V20c0 .6-.4 1-1 1A17 17 0 013 4c0-.6.4-1 1-1h3.5c.6 0 1 .4 1 1 0 1.3.2 2.5.6 3.6.1.3 0 .7-.2 1z"/></svg>
    +1 8888-888-888
  </span>
  <span style="left:803px">|</span>
  <span style="left:834px">
    <svg width="15" height="12" viewBox="0 0 24 18" fill="#fff"><path d="M0 0h24v18H0z" opacity="0"/><path d="M2 0h20a2 2 0 012 2v.5L12 9 0 2.5V2a2 2 0 012-2zM0 5l12 6.5L24 5v11a2 2 0 01-2 2H2a2 2 0 01-2-2z"/></svg>
    info@houndridgedetection.com
  </span>
</div>

<div class="abs navbar">
  <a class="nav-item active" style="left:342px">Home</a>
  <a class="nav-item" style="left:424px">About Us</a>
  <a class="nav-item" style="left:525px">Services</a>
  <a class="nav-item" style="left:620px">Educational Resources</a>
  <a class="nav-item" style="left:815px">Testimonials</a>
  <a class="nav-item" style="left:941px">FAQs</a>
  <a class="nav-item" style="left:1015px">Contact Us</a>
</div>
<div class="abs brand"><div class="brand-circle">Hound Ridge Detection Services</div></div>

<div class="abs hero" role="img" aria-label="Detection dog wearing a harness in a school hallway with a student and backpack"></div>
<h1 class="abs hero-title">Expert K9 Detection<br>For Safer Schools</h1>
<p class="abs hero-text">Lorem ipsum dolor sit amet, consectetur adipiscing elit, sed do eiusmod tempor incididunt</p>
<a class="abs btn hero-btn">Get Started</a>

<h2 class="abs section-title" style="top:692px">Our Services</h2>

<div class="abs service-card" style="left:110px;top:781px">
  <div class="icon-circle"><svg width="50" height="50" viewBox="0 0 50 50" fill="none" stroke="#fff" stroke-width="2"><rect x="13" y="8" width="16" height="6"/><path d="M15 14h12v6l3 4v18H12V24l3-4z"/><path d="M21 27v8M17 31h8"/><rect x="28" y="30" width="14" height="8" rx="4" transform="rotate(-30 35 34)"/></svg></div>
  <h3>Drug Detection</h3>
  <p>Lorem ipsum dolor sit amet, consectetur adipiscing elit, sed do eiusmod tempor</p>
  <a class="more">Read More</a>
</div>
<div class="abs service-card" style="left:361px;top:833px">
  <div class="icon-circle"><svg width="50" height="50" viewBox="0 0 50 50" fill="none" stroke="#fff" stroke-width="2"><path d="M10 40l24-24 6 6-24 24z" transform="translate(-2 -4)"/><path d="M34 10l6 6M36 8l6 6"/><path d="M20 30l4 4"/></svg></div>
  <h3>Vape Detection</h3>
  <p>Lorem ipsum dolor sit amet, consectetur adipiscing elit, sed do eiusmod tempor</p>
  <a class="more">Read More</a>
</div>
<div class="abs service-card" style="left:609px;top:781px">
  <div class="icon-circle"><svg width="50" height="50" viewBox="0 0 50 50" fill="none" stroke="#fff" stroke-width="2"><rect x="10" y="12" width="26" height="26" rx="3"/><path d="M18 12V8h10v4M14 20h18M14 26h10"/><circle cx="33" cy="31" r="7"/><circle cx="33" cy="31" r="2"/><path d="M38 36l5 5"/></svg></div>
  <h3>Contraband Detection</h3>
  <p>Lorem ipsum dolor sit amet, consectetur adipiscing elit, sed do eiusmod tempor</p>
  <a class="more">Read More</a>
</div>
<div class="abs service-card" style="left:858px;top:833px">
  <div class="icon-circle"><svg width="50" height="50" viewBox="0 0 50 50" fill="none" stroke="#fff" stroke-width="2"><path d="M16 22a8 8 0 0116 0v6H16z"/><path d="M12 28h24v4H12zM24 8v4M12 14l3 3M36 14l-3 3"/><circle cx="33" cy="38" r="5"/><path d="M10 42h16"/></svg></div>
  <h3>Emergency Response</h3>
  <p>Lorem ipsum dolor sit amet, consectetur adipiscing elit, sed do eiusmod tempor</p>
  <a class="more">Read More</a>
</div>

<div class="abs edu" role="img" aria-label="Blue band with a faint dog portrait in the background"></div>
<svg class="abs edu-ring" viewBox="0 0 430 420"><path d="M215 12 A200 200 0 0 1 215 408" fill="none" stroke="#1b86d6" stroke-width="14"/><circle cx="199" cy="209" r="203" fill="none" stroke="#fff" stroke-width="14"/></svg>
<div class="abs edu-photo" role="img" aria-label="Children with backpacks running down a school hallway"></div>
<h2 class="abs edu-title">Educational</h2>
<p class="abs edu-text">Sed ut perspiciatis unde omnis iste natus error sit voluptatem accusantium doloremque laudantium, totam rem aperiam, eaque ipsa quae ab illo inventore veritatis et quasi architecto beatae vitae dicta sunt explicabo. Nemo enim ipsam voluptatem quia voluptas sit aspernatur aut odit aut fugit, sed quia consequuntur magni dolores eos qui ratione voluptatem sequi nesciunt. Neque porro quisquam est, qui dolorem ipsum quia dolor sit amet, consectetur, adipisci velit, sed quia non numquam eius modi tempora incidunt ut labore et dolore magnam aliquam quaerat voluptatem.</p>
<a class="abs btn edu-btn">Read More</a>

<div class="abs plans"></div>
<h2 class="abs section-title" style="top:1880px">Service Plans</h2>

<div class="abs plan" style="left:112px">
  <h3>Basic Plan</h3><div class="sub">Monthly K9 detection sweeps</div><hr>
  <ul>
    <li><svg width="14" height="14" viewBox="0 0 14 14"><rect x="1" y="1" width="12" height="12" rx="2" fill="none" stroke="#0677BA" stroke-width="1.4"/><path d="M4 7l2 2 4-4" fill="none" stroke="#0677BA" stroke-width="1.4"/></svg>Excepteur sint occae sint</li>
    <li><svg width="14" height="14" viewBox="0 0 14 14"><rect x="1" y="1" width="12" height="12" rx="2" fill="none" stroke="#0677BA" stroke-width="1.4"/><path d="M4 7l2 2 4-4" fill="none" stroke="#0677BA" stroke-width="1.4"/></svg>Ut enim ad minima</li>
    <li><svg width="14" height="14" viewBox="0 0 14 14"><rect x="1" y="1" width="12" height="12" rx="2" fill="none" stroke="#0677BA" stroke-width="1.4"/><path d="M4 7l2 2 4-4" fill="none" stroke="#0677BA" stroke-width="1.4"/></svg>Quis autem vel eum ullam corp</li>
    <li><svg width="14" height="14" viewBox="0 0 14 14"><rect x="1" y="1" width="12" height="12" rx="2" fill="none" stroke="#0677BA" stroke-width="1.4"/><path d="M4 7l2 2 4-4" fill="none" stroke="#0677BA" stroke-width="1.4"/></svg>Sed ut perspicia eius modi</li>
    <li><svg width="14" height="14" viewBox="0 0 14 14"><rect x="1" y="1" width="12" height="12" rx="2" fill="none" stroke="#0677BA" stroke-width="1.4"/><path d="M4 7l2 2 4-4" fill="none" stroke="#0677BA" stroke-width="1.4"/></svg>Excepteur sint occae sint</li>
    <li><svg width="14" height="14" viewBox="0 0 14 14"><rect x="1" y="1" width="12" height="12" rx="2" fill="none" stroke="#0677BA" stroke-width="1.4"/><path d="M4 7l2 2 4-4" fill="none" stroke="#0677BA" stroke-width="1.4"/></svg>Ut enim ad minima</li>
    <li><svg width="14" height="14" viewBox="0 0 14 14"><rect x="1" y="1" width="12" height="12" rx="2" fill="none" stroke="#0677BA" stroke-width="1.4"/><path d="M4 7l2 2 4-4" fill="none" stroke="#0677BA" stroke-width="1.4"/></svg>Quis autem vel eum ullam corp</li>
    <li><svg width="14" height="14" viewBox="0 0 14 14"><rect x="1" y="1" width="12" height="12" rx="2" fill="none" stroke="#0677BA" stroke-width="1.4"/><path d="M4 7l2 2 4-4" fill="none" stroke="#0677BA" stroke-width="1.4"/></svg>Sed ut perspicia eius modi</li>
  </ul>
  <div class="line-bottom"></div>
  <a class="btn">Get Started</a>
</div>

<div class="abs plan featured" style="left:451px">
  <h3>Premium Plan</h3><div class="sub">Weekly K9 detection sweeps.</div><hr>
  <ul>
    <li><svg width="14" height="14" viewBox="0 0 14 14"><rect x="1" y="1" width="12" height="12" rx="2" fill="none" stroke="#fff" stroke-width="1.4"/><path d="M4 7l2 2 4-4" fill="none" stroke="#fff" stroke-width="1.4"/></svg>Excepteur sint occae sint</li>
    <li><svg width="14" height="14" viewBox="0 0 14 14"><rect x="1" y="1" width="12" height="12" rx="2" fill="none" stroke="#fff" stroke-width="1.4"/><path d="M4 7l2 2 4-4" fill="none" stroke="#fff" stroke-width="1.4"/></svg>Ut enim ad minima</li>
    <li><svg width="14" height="14" viewBox="0 0 14 14"><rect x="1" y="1" width="12" height="12" rx="2" fill="none" stroke="#fff" stroke-width="1.4"/><path d="M4 7l2 2 4-4" fill="none" stroke="#fff" stroke-width="1.4"/></svg>Quis autem vel eum ullam corp</li>
    <li><svg width="14" height="14" viewBox="0 0 14 14"><rect x="1" y="1" width="12" height="12" rx="2" fill="none" stroke="#fff" stroke-width="1.4"/><path d="M4 7l2 2 4-4" fill="none" stroke="#fff" stroke-width="1.4"/></svg>Sed ut perspicia eius modi</li>
    <li><svg width="14" height="14" viewBox="0 0 14 14"><rect x="1" y="1" width="12" height="12" rx="2" fill="none" stroke="#fff" stroke-width="1.4"/><path d="M4 7l2 2 4-4" fill="none" stroke="#fff" stroke-width="1.4"/></svg>Excepteur sint occae sint</li>
    <li><svg width="14" height="14" viewBox="0 0 14 14"><rect x="1" y="1" width="12" height="12" rx="2" fill="none" stroke="#fff" stroke-width="1.4"/><path d="M4 7l2 2 4-4" fill="none" stroke="#fff" stroke-width="1.4"/></svg>Ut enim ad minima</li>
    <li><svg width="14" height="14" viewBox="0 0 14 14"><rect x="1" y="1" width="12" height="12" rx="2" fill="none" stroke="#fff" stroke-width="1.4"/><path d="M4 7l2 2 4-4" fill="none" stroke="#fff" stroke-width="1.4"/></svg>Quis autem vel eum ullam corp</li>
    <li><svg width="14" height="14" viewBox="0 0 14 14"><rect x="1" y="1" width="12" height="12" rx="2" fill="none" stroke="#fff" stroke-width="1.4"/><path d="M4 7l2 2 4-4" fill="none" stroke="#fff" stroke-width="1.4"/></svg>Sed ut perspicia eius modi</li>
  </ul>
  <div class="line-bottom"></div>
  <a class="btn">Get Started</a>
</div>

<div class="abs plan" style="left:789px">
  <h3>Standard Plan</h3><div class="sub">Bi-weekly K9 detection sweeps.</div><hr>
  <ul>
    <li><svg width="14" height="14" viewBox="0 0 14 14"><rect x="1" y="1" width="12" height="12" rx="2" fill="none" stroke="#0677BA" stroke-width="1.4"/><path d="M4 7l2 2 4-4" fill="none" stroke="#0677BA" stroke-width="1.4"/></svg>Excepteur sint occae sint</li>
    <li><svg width="14" height="14" viewBox="0 0 14 14"><rect x="1" y="1" width="12" height="12" rx="2" fill="none" stroke="#0677BA" stroke-width="1.4"/><path d="M4 7l2 2 4-4" fill="none" stroke="#0677BA" stroke-width="1.4"/></svg>Ut enim ad minima</li>
    <li><svg width="14" height="14" viewBox="0 0 14 14"><rect x="1" y="1" width="12" height="12" rx="2" fill="none" stroke="#0677BA" stroke-width="1.4"/><path d="M4 7l2 2 4-4" fill="none" stroke="#0677BA" stroke-width="1.4"/></svg>Quis autem vel eum ullam corp</li>
    <li><svg width="14" height="14" viewBox="0 0 14 14"><rect x="1" y="1" width="12" height="12" rx="2" fill="none" stroke="#0677BA" stroke-width="1.4"/><path d="M4 7l2 2 4-4" fill="none" stroke="#0677BA" stroke-width="1.4"/></svg>Sed ut perspicia eius modi</li>
    <li><svg width="14" height="14" viewBox="0 0 14 14"><rect x="1" y="1" width="12" height="12" rx="2" fill="none" stroke="#0677BA" stroke-width="1.4"/><path d="M4 7l2 2 4-4" fill="none" stroke="#0677BA" stroke-width="1.4"/></svg>Excepteur sint occae sint</li>
    <li><svg width="14" height="14" viewBox="0 0 14 14"><rect x="1" y="1" width="12" height="12" rx="2" fill="none" stroke="#0677BA" stroke-width="1.4"/><path d="M4 7l2 2 4-4" fill="none" stroke="#0677BA" stroke-width="1.4"/></svg>Ut enim ad minima</li>
    <li><svg width="14" height="14" viewBox="0 0 14 14"><rect x="1" y="1" width="12" height="12" rx="2" fill="none" stroke="#0677BA" stroke-width="1.4"/><path d="M4 7l2 2 4-4" fill="none" stroke="#0677BA" stroke-width="1.4"/></svg>Quis autem vel eum ullam corp</li>
    <li><svg width="14" height="14" viewBox="0 0 14 14"><rect x="1" y="1" width="12" height="12" rx="2" fill="none" stroke="#0677BA" stroke-width="1.4"/><path d="M4 7l2 2 4-4" fill="none" stroke="#0677BA" stroke-width="1.4"/></svg>Sed ut perspicia eius modi</li>
  </ul>
  <div class="line-bottom"></div>
  <a class="btn">Get Started</a>
</div>

<h2 class="abs section-title" style="top:2556px">Client Reviews</h2>

<div class="abs review" style="left:-379px">
  <p>“Sed ut perspiciatis unde omnis iste natus error sit voluptatem accusantium doloremque laudantium, totam rem aperiam, eaque ipsa quae ab illo inventore veritatis et quasi architecto beatae vitae dicta sunt explicabo.”</p>
  <svg style="position:absolute;left:404px;top:158px" width="36" height="28" viewBox="0 0 36 28"><path d="M2 2h13v13c0 7-4 11-11 12l-1-4c4-1 6-3 6-7H2zM20 2h13v13c0 7-4 11-11 12l-1-4c4-1 6-3 6-7h-7z" fill="#111"/></svg>
</div>

<div class="abs review" style="left:126px">
  <div class="tail"></div>
  <svg style="position:absolute;left:16px;top:14px" width="36" height="28" viewBox="0 0 36 28"><path d="M34 26H21V13C21 6 25 2 32 1l1 4c-4 1-6 3-6 7h7zM16 26H3V13C3 6 7 2 14 1l1 4c-4 1-6 3-6 7h7z" fill="#111"/></svg>
  <p>“Sed ut perspiciatis unde omnis iste natus error sit voluptatem accusantium doloremque laudantium, totam rem aperiam, eaque ipsa quae ab illo inventore veritatis et quasi architecto beatae vitae dicta sunt explicabo.”</p>
  <div class="stars"><svg width="18" height="18" viewBox="0 0 24 24"><path d="M12 2l3 7 7 .6-5.4 4.7 1.7 7.2L12 17.8 5.7 21.5l1.7-7.2L2 9.6 9 9z" fill="#f5a623"/></svg>5.5 Reviews</div>
  <svg style="position:absolute;left:400px;top:158px" width="36" height="28" viewBox="0 0 36 28"><path d="M2 2h13v13c0 7-4 11-11 12l-1-4c4-1 6-3 6-7H2zM20 2h13v13c0 7-4 11-11 12l-1-4c4-1 6-3 6-7h-7z" fill="#111"/></svg>
</div>
<div class="abs reviewer" style="left:159px;top:2887px">
  <div class="avatar" role="img" aria-label="Client portrait"></div>
  <div><h4>Jordan Vale</h4><span>Ut enim ad minima veniam</span></div>
</div>

<div class="abs review" style="left:629px">
  <div class="tail"></div>
  <svg style="position:absolute;left:16px;top:14px" width="36" height="28" viewBox="0 0 36 28"><path d="M34 26H21V13C21 6 25 2 32 1l1 4c-4 1-6 3-6 7h7zM16 26H3V13C3 6 7 2 14 1l1 4c-4 1-6 3-6 7h7z" fill="#111"/></svg>
  <p>“Sed ut perspiciatis unde omnis iste natus error sit voluptatem accusantium doloremque laudantium, totam rem aperiam, eaque ipsa quae ab illo inventore veritatis et quasi architecto beatae vitae dicta sunt explicabo.”</p>
  <div class="stars"><svg width="18" height="18" viewBox="0 0 24 24"><path d="M12 2l3 7 7 .6-5.4 4.7 1.7 7.2L12 17.8 5.7 21.5l1.7-7.2L2 9.6 9 9z" fill="#f5a623"/></svg>5.5 Reviews</div>
  <svg style="position:absolute;left:400px;top:158px" width="36" height="28" viewBox="0 0 36 28"><path d="M2 2h13v13c0 7-4 11-11 12l-1-4c4-1 6-3 6-7H2zM20 2h13v13c0 7-4 11-11 12l-1-4c4-1 6-3 6-7h-7z" fill="#111"/></svg>
</div>
<div class="abs reviewer" style="left:663px;top:2887px">
  <div class="avatar" role="img" aria-label="Client portrait"></div>
  <div><h4>Jordan Vale</h4><span>Ut enim ad minima veniam</span></div>
</div>

<div class="abs review" style="left:1133px">
  <div class="tail"></div>
  <svg style="position:absolute;left:16px;top:14px" width="36" height="28" viewBox="0 0 36 28"><path d="M34 26H21V13C21 6 25 2 32 1l1 4c-4 1-6 3-6 7h7zM16 26H3V13C3 6 7 2 14 1l1 4c-4 1-6 3-6 7h7z" fill="#111"/></svg>
  <p>“Sed ut perspiciatis unde omnis iste natus error sit voluptatem accusantium doloremque laudantium, totam rem aperiam, eaque ipsa quae ab illo inventore veritatis et quasi architecto.”</p>
  <div class="stars"><svg width="18" height="18" viewBox="0 0 24 24"><path d="M12 2l3 7 7 .6-5.4 4.7 1.7 7.2L12 17.8 5.7 21.5l1.7-7.2L2 9.6 9 9z" fill="#f5a623"/></svg>5.5 Reviews</div>
</div>
<div class="abs avatar" style="left:1166px;top:2887px" role="img" aria-label="Client portrait"></div>

<div class="abs divider"></div>

<h2 class="abs faq-title">Frequently Asked Questions</h2>
<div class="abs faq" style="top:3190px">Q:1 Duis aute irure dolor in reprehenderit<svg width="14" height="9" viewBox="0 0 14 9"><path d="M1 1l6 6 6-6" fill="none" stroke="#333" stroke-width="2"/></svg></div>
<div class="abs faq" style="top:3254px">Q:2 Excepteur sint occaecat cupidatat non proident<svg width="14" height="9" viewBox="0 0 14 9"><path d="M1 1l6 6 6-6" fill="none" stroke="#333" stroke-width="2"/></svg></div>
<div class="abs faq" style="top:3318px">Q:3 Nemo enim ipsam voluptatem quia voluptas sit<svg width="14" height="9" viewBox="0 0 14 9"><path d="M1 1l6 6 6-6" fill="none" stroke="#333" stroke-width="2"/></svg></div>
<div class="abs faq" style="top:3381px">Q:4 Duis aute irure dolor in reprehenderit<svg width="14" height="9" viewBox="0 0 14 9"><path d="M1 1l6 6 6-6" fill="none" stroke="#333" stroke-width="2"/></svg></div>
<div class="abs faq" style="top:3445px">Q:5 Excepteur sint occaecat cupidatat non proident<svg width="14" height="9" viewBox="0 0 14 9"><path d="M1 1l6 6 6-6" fill="none" stroke="#333" stroke-width="2"/></svg></div>
<div class="abs faq-dog" role="img" aria-label="German shepherd lying down, facing forward"></div>

<div class="abs footer"></div>
<div class="abs foot-brand" style="color:#fff"><span class="dot"></span>Hound Ridge Detection Services</div>
<div class="abs socials" role="img" aria-label="Social media links"><span></span><span></span><span></span><span></span><span></span></div>

<div class="abs footer-col" style="left:379px;top:3651px;color:#fff">
  <h4 style="font-size:20px;font-weight:500">Quick Links</h4>
  <ul style="list-style:none;margin-top:28px;font-size:14px;line-height:26px">
    <li>Home</li><li>About Us</li><li>Services</li><li>Educational Resources</li><li>Testimonials</li>
  </ul>
</div>
<div class="abs footer-col" style="left:612px;top:3651px;color:#fff">
  <h4 style="font-size:20px;font-weight:500">Other Links</h4>
  <ul style="list-style:none;margin-top:28px;font-size:14px;line-height:26px">
    <li>FAQs</li><li>Contact Us</li><li>Terms &amp; Conditions</li><li>Privacy Policy</li><li>Sitemaps</li>
  </ul>
</div>
<div class="abs footer-col" style="left:833px;top:3651px;color:#fff">
  <h4 style="font-size:20px;font-weight:500">Contact Info</h4>
  <div style="margin-top:28px">
    <div class="contact-row"><svg width="12" height="16" viewBox="0 0 12 16" style="flex:none;margin-top:3px"><path d="M6 0a6 6 0 016 6c0 4-6 10-6 10S0 10 0 6a6 6 0 016-6zm0 4a2 2 0 100 4 2 2 0 000-4z" fill="#fff"/></svg><span>158, Ut enim ad minima veniam,<br>quis nostrum exercita.</span></div>
    <div class="contact-row"><svg width="14" height="14" viewBox="0 0 24 24" style="flex:none;margin-top:3px" fill="#fff"><path d="M6.6 10.8a15.1 15.1 0 006.6 6.6l2.2-2.2c.3-.3.7-.4 1-.2 1.1.4 2.3.6 3.6.6.6 0 1 .4 1 1V20c0 .6-.4 1-1 1A17 17 0 013 4c0-.6.4-1 1-1h3.5c.6 0 1 .4 1 1 0 1.3.2 2.5.6 3.6.1.3 0 .7-.2 1z"/></svg><span>+1 8888-888-888</span></div>
    <div class="contact-row"><svg width="14" height="11" viewBox="0 0 24 18" style="flex:none;margin-top:5px" fill="#fff"><path d="M2 0h20a2 2 0 012 2v.5L12 9 0 2.5V2a2 2 0 012-2zM0 5l12 6.5L24 5v11a2 2 0 01-2 2H2a2 2 0 01-2-2z"/></svg><span>info@houndridgedetection.com</span></div>
  </div>
</div>
<div class="abs copy" style="color:#fff">Copyright © 2025 Hound Ridge Detection Services. All rights reserved.</div>

</body>
</html>
```